Creative, Fun, Eye catching signage for new office - inspire and inform!

I am looking for a billboard sign, a smaller sign and a very small sign for parking spots. These will be located in our new office space. I have uploaded two logos, this way you can choose. I would love to see what it looks like with black behind the logo but am open to creative ideas. I would like the majority of the background to be black and/or white

1. Sign for over door – with five at the top like in the photo attached

The sign size is 2600mm (L) x 900mm (H)

Logo at the top then services to the right side
Social & Living Skills Programs
Support Workers
Respite/Supported Holidays
Exercise Physiology
Occupational Therapy
Speech Therapy
Psychology
Behavioural Therapy

I would like the design to tie in with the website and/or flyers/banners attached. Please also try and add 1800 452 917

2. Sign for glass roller door

745cm wide by 725cm high ( similar to what next door has without it saying parent )

Tellwick Logo
Drop Off Zone

Smaller signs for parking spots
1000cm wide, 60cm high

Tellwick logo Visitor Parking 24/7

I would like the design to be consistent across the three items so they work together but are not identical.

I have attached images showing what I am talking about in relation to the location of each sign.

Target Market(s)

Families, parents and people with disabilities

Industry/Entity Type

Disability and community service

Colors

Designer to choose colors to be used in the design.

Requirements
Must have
• White or black background - the logo and please use colours shown in the brochures and banners provided. Preferences are black white and yellow
Nice to have
• all of our services and website and/or 1800 452 917 on banner 1
Should not have
• I dont want it to be to busy please

```html
<!DOCTYPE html>
<html lang="en">
<head>
<meta charset="utf-8">
<title>Tellwick Signage Set</title>
<link rel="stylesheet" href="https://fonts.googleapis.com/css2?family=Fira+Sans:wght@400;600;800&display=swap">
<style>
  :root {
    --sun-yellow: #fcc33b;
    --sign-black: #050607;
    --text-white: #ffffff;
    --shadow: rgba(90, 60, 0, 0.35);
  }
  * { margin: 0; padding: 0; box-sizing: border-box; }
  html, body { width: 1189px; height: 1200px; overflow: hidden; }
  body {
    position: relative;
    background: var(--sun-yellow);
    font-family: "Fira Sans", Arial, sans-serif;
  }
  .sign {
    position: absolute;
    background: var(--sign-black);
    box-shadow: 10px 12px 14px var(--shadow);
  }
  .abs { position: absolute; }
  .brand-dot { position: absolute; border-radius: 50%; background: var(--sun-yellow); }
  .brand-name {
    position: absolute;
    color: var(--text-white);
    font-weight: 800;
    letter-spacing: 1px;
    line-height: 1;
    white-space: nowrap;
  }
  .pill {
    position: absolute;
    background: var(--sun-yellow);
    border-radius: 10px;
    display: flex;
    align-items: center;
  }
  .phone-number {
    color: var(--text-white);
    font-weight: 600;
    line-height: 1;
    white-space: nowrap;
  }
  .phone-icon { position: absolute; }

  /* Over-door billboard */
  .billboard { left: 74px; top: 79px; width: 1040px; height: 368px; }
  .services-tag {
    left: 576px; top: 32px; width: 175px; height: 41px;
    background: var(--sun-yellow); border-radius: 9px;
    display: flex; align-items: center; justify-content: center;
    font-weight: 600; font-size: 22px; color: var(--sign-black);
  }
  .services-list { left: 575px; top: 84px; list-style: none; }
  .services-list li {
    display: flex; align-items: center;
    height: 29.6px; font-size: 18.5px; color: var(--text-white);
  }
  .services-list li::before {
    content: ""; width: 15px; height: 15px; border-radius: 50%;
    background: var(--sun-yellow); margin-right: 9px; flex: none;
  }

  /* Roller door sign */
  .door-sign { left: 362px; top: 509px; width: 464px; height: 451px; }
  .zone-label {
    left: 99px; top: 258px; width: 267px; height: 61px;
    justify-content: center; font-size: 37px; color: var(--sign-black);
  }

  /* Parking strip */
  .parking-sign { left: 46px; top: 1030px; width: 1096px; height: 72px; }
  .parking-label {
    left: 293px; top: 10px; width: 380px; height: 53px;
    justify-content: center; font-size: 34px; color: var(--sign-black);
  }
</style>
</head>
<body>

<!-- Over-door billboard -->
<section class="sign billboard">
  <div class="brand-dot" style="left:313px; top:32px; width:96px; height:96px;"></div>
  <div class="brand-name" style="left:56px; top:162px; font-size:94px; width:450px; text-align:center;">TELLWICK</div>

  <div class="pill" style="left:128px; top:276px; width:366px; height:60px; padding-left:48px;">
    <span class="phone-number" style="font-size:48px;">1800 452 917</span>
  </div>
  <svg class="phone-icon" style="left:72px; top:272px;" width="68" height="68" viewBox="0 0 68 68" aria-hidden="true">
    <circle cx="34" cy="34" r="31" fill="#fcc33b" stroke="#050607" stroke-width="5"/>
    <path d="M22 18c3-2 5 0 7 4l2 4c1 2 0 4-2 5l-2 1c1 4 5 8 9 10l1-2c1-2 3-3 5-2l4 2c4 2 5 4 3 7-3 4-7 5-12 3-8-4-14-10-17-18-2-5-1-11 2-14z" fill="#050607"/>
    <path d="M37 19a12 12 0 0 1 12 12M37 13a18 18 0 0 1 18 18" fill="none" stroke="#050607" stroke-width="2.5" stroke-linecap="round"/>
  </svg>

  <div class="abs services-tag">OUR SERVICES</div>
  <ul class="abs services-list">
    <li>Logo at the top then services to the right side</li>
    <li>Social &amp; Living Skills Programs</li>
    <li>Support Workers</li>
    <li>Respite/Supported Holidays</li>
    <li>Exercise Physiology</li>
    <li>Occupational Therapy</li>
    <li>Speech Therapy</li>
    <li>Psychology</li>
    <li>Behavioural Therapy</li>
  </ul>
</section>

<!-- Roller door sign -->
<section class="sign door-sign">
  <div class="brand-dot" style="left:257px; top:41px; width:78px; height:78px;"></div>
  <div class="brand-name" style="left:32px; top:138px; font-size:78px; width:400px; text-align:center;">TELLWICK</div>

  <div class="pill zone-label">Drop Off Zone</div>

  <div class="pill" style="left:88px; top:357px; width:336px; height:56px; padding-left:60px;">
    <span class="phone-number" style="font-size:42px;">1800 452 917</span>
  </div>
  <svg class="phone-icon" style="left:37px; top:355px;" width="60" height="60" viewBox="0 0 68 68" aria-hidden="true">
    <circle cx="34" cy="34" r="31" fill="#fcc33b" stroke="#050607" stroke-width="5"/>
    <path d="M22 18c3-2 5 0 7 4l2 4c1 2 0 4-2 5l-2 1c1 4 5 8 9 10l1-2c1-2 3-3 5-2l4 2c4 2 5 4 3 7-3 4-7 5-12 3-8-4-14-10-17-18-2-5-1-11 2-14z" fill="#050607"/>
    <path d="M37 19a12 12 0 0 1 12 12M37 13a18 18 0 0 1 18 18" fill="none" stroke="#050607" stroke-width="2.5" stroke-linecap="round"/>
  </svg>
</section>

<!-- Parking strip -->
<section class="sign parking-sign">
  <div class="brand-dot" style="left:10px; top:12px; width:48px; height:48px;"></div>
  <div class="brand-name" style="left:68px; top:17px; font-size:39px;">TELLWICK</div>

  <div class="pill parking-label">Visitor Parking 24/7</div>

  <div class="pill" style="left:764px; top:10px; width:323px; height:53px; padding-left:54px;">
    <span class="phone-number" style="font-size:42px;">1800 452 917</span>
  </div>
  <svg class="phone-icon" style="left:719px; top:6px;" width="60" height="60" viewBox="0 0 68 68" aria-hidden="true">
    <circle cx="34" cy="34" r="31" fill="#fcc33b" stroke="#050607" stroke-width="5"/>
    <path d="M22 18c3-2 5 0 7 4l2 4c1 2 0 4-2 5l-2 1c1 4 5 8 9 10l1-2c1-2 3-3 5-2l4 2c4 2 5 4 3 7-3 4-7 5-12 3-8-4-14-10-17-18-2-5-1-11 2-14z" fill="#050607"/>
    <path d="M37 19a12 12 0 0 1 12 12M37 13a18 18 0 0 1 18 18" fill="none" stroke="#050607" stroke-width="2.5" stroke-linecap="round"/>
  </svg>
</section>

</body>
</html>
```